Canadian Christian Church needs design for new sermon series

A graphic design for our series and an invitation card to invite people to the series. Check design brief for more detailed information. Target audience: young families and young adults. Looking for a creative design that will get people's attention and create interest. See design brief for copy of design purchased for previous series.
Updates
entered Apr 4 incorrectly. Need a week to receive and review designs, and today is Apr 2/19. Thanks!
Target Market(s)
young families and young adults
Colors
Designer to choose colors to be used in the design.
Look and feel

```html
<!DOCTYPE html>
<html lang="en">
<head>
<meta charset="utf-8">
<title>Messy – Sermon Series Invitation</title>
<link href="https://fonts.googleapis.com/css2?family=Montserrat:wght@400;500;600&family=Oswald:wght@700&family=Roboto+Slab:wght@400;700&display=block" rel="stylesheet">
<style>
  :root {
    --backdrop: #7a7a7a;
    --orange: #f28a1c;
    --orange-light: #fbb934;
    --purple: #6a2c8c;
    --charcoal: #2e2d33;
    --beige-light: #ddd4bd;
    --beige-dark: #c6bb9f;
    --ink: #2b2622;
    --brown: #3b312d;
    --blue: #1f7fcf;
    --white: #ffffff;
  }
  * { box-sizing: border-box; margin: 0; padding: 0; }
  html, body { width: 1200px; height: 903px; overflow: hidden; }
  body { background: var(--backdrop); position: relative; font-family: "Montserrat", sans-serif; }

  .card { position: absolute; width: 483px; height: 378px; overflow: hidden; box-shadow: 0 2px 6px rgba(0,0,0,.35); }

  /* Front */
  .card-front { left: 237px; top: 61px; background: var(--charcoal); }
  .hero-photo { position: absolute; left: 0; top: 0; width: 483px; height: 312px;
    background:
      radial-gradient(ellipse 38% 30% at 18% 22%, rgba(255,255,255,.95) 0%, rgba(255,255,255,0) 100%),
      radial-gradient(ellipse 22% 26% at 60% 60%, rgba(236,170,160,.75) 0%, rgba(236,170,160,0) 100%),
      radial-gradient(ellipse 14% 18% at 92% 42%, rgba(40,110,200,.55) 0%, rgba(40,110,200,0) 100%),
      radial-gradient(ellipse 30% 22% at 12% 92%, rgba(60,80,70,.55) 0%, rgba(60,80,70,0) 100%),
      radial-gradient(ellipse 30% 24% at 72% 92%, rgba(120,150,190,.5) 0%, rgba(120,150,190,0) 100%),
      radial-gradient(ellipse 20% 30% at 90% 10%, rgba(70,70,75,.55) 0%, rgba(70,70,75,0) 100%),
      linear-gradient(175deg, #f6f5f2 0%, #e7e3dc 35%, #c9b79c 62%, #a89074 100%); }
  .church-name { position: absolute; left: 30px; top: 100px; display: flex; align-items: center; gap: 7px;
    font-family: "Roboto Slab", serif; font-size: 12px; color: var(--ink); }
  .church-name .dot { width: 14px; height: 14px; border-radius: 50%; background: var(--orange); }
  .series-title { position: absolute; left: 262px; top: 26px; font-family: "Oswald", sans-serif; font-weight: 700;
    font-size: 76px; line-height: 1; letter-spacing: 0; color: var(--orange);
    background: linear-gradient(180deg, var(--orange-light), var(--orange));
    -webkit-background-clip: text; background-clip: text; -webkit-text-fill-color: transparent;
    -webkit-text-stroke: 2.5px var(--purple); transform: scaleY(1.05); }
  .tagline { position: absolute; left: 0; top: 312px; width: 483px; height: 66px;
    display: flex; align-items: center; justify-content: center;
    font-family: "Roboto Slab", serif; font-size: 36px; color: var(--orange); }

  /* Back */
  .card-back { left: 582px; top: 469px;
    background: radial-gradient(ellipse at 70% 40%, var(--beige-light) 0%, var(--beige-dark) 100%); }
  .service-heading { position: absolute; top: 24px; width: 100%; text-align: center;
    font-family: "Roboto Slab", serif; font-weight: 700; color: var(--ink); font-size: 25px; line-height: 32px; }
  .service-heading .time { font-size: 26px; }
  .section-label { position: absolute; left: 27px; font-size: 11.5px; font-weight: 600; color: var(--ink); }
  .label-sermons { top: 102px; }
  .label-features { top: 257px; }
  .sermon-table { position: absolute; left: 27px; top: 118px; width: 227px; border-collapse: collapse;
    font-size: 10.5px; color: var(--ink); }
  .sermon-table td { border: 1px solid #6e6556; height: 15.8px; padding: 0 6px; white-space: nowrap; }
  .sermon-table td.date { width: 76px; }
  .feature-list { position: absolute; left: 28px; top: 273px; list-style: none; font-size: 11px; color: #4a433b; }
  .feature-list li { display: flex; align-items: center; gap: 6px; line-height: 14.6px; }
  .feature-list svg { flex: none; }
  .core-values { position: absolute; left: 288px; top: 108px; width: 173px; height: 166px; border-radius: 50%;
    background: conic-gradient(var(--orange), var(--blue), var(--purple), var(--orange)); opacity: .9; }
  .contact-band { position: absolute; left: 0; top: 326px; width: 100%; height: 52px; background: var(--brown);
    color: var(--white); font-size: 9.6px; text-align: center; padding-top: 10px; line-height: 17px; }
</style>
</head>
<body>

<section class="card card-front">
  <div class="hero-photo" role="img" aria-label="Photo of a young woman sitting on the floor of a cluttered room, hands on her head, surrounded by scattered clothes and boxes"></div>
  <div class="church-name"><span class="dot"></span>Maple Grove Family Church</div>
  <div class="series-title">MESSY</div>
  <div class="tagline">Joining God in the Mess</div>
</section>

<section class="card card-back">
  <h1 class="service-heading">THE TIME OF THE SERVICES:<br><span class="time">Sundays @ 10:30</span></h1>
  <p class="section-label label-sermons">Names &amp; Dates of the sermons:</p>
  <table class="sermon-table">
    <tr><td class="date">April 28th:</td><td>We Made This Mess</td></tr>
    <tr><td class="date">May 5th:</td><td>Bless in the Mess</td></tr>
    <tr><td class="date">May 12th:</td><td>Born into the Mess</td></tr>
    <tr><td class="date">May 19th:</td><td>Messy Work</td></tr>
    <tr><td class="date">May 26th:</td><td>Messy Church</td></tr>
    <tr><td class="date">June 2nd:</td><td>Messy Hospitality</td></tr>
    <tr><td class="date">June 9th:</td><td>TBD</td></tr>
    <tr><td class="date">June 16th:</td><td>Messy within Boundaries</td></tr>
  </table>
  <div class="core-values" role="img" aria-label="Core values diagram of interlocking coloured ribbons: Equipping, Serving, Missional Living, Spirit-Living, Belonging"></div>
  <p class="section-label label-features">Features of the service:</p>
  <ul class="feature-list">
    <li><svg width="8" height="8" viewBox="0 0 8 8"><circle cx="4" cy="4" r="4" fill="var(--blue)"/><path d="M2.2 4.1l1.2 1.2 2.4-2.5" stroke="#fff" stroke-width="1" fill="none"/></svg>Staffed nursery &amp; children’s program every Sunday</li>
    <li><svg width="8" height="8" viewBox="0 0 8 8"><circle cx="4" cy="4" r="4" fill="var(--blue)"/><path d="M2.2 4.1l1.2 1.2 2.4-2.5" stroke="#fff" stroke-width="1" fill="none"/></svg>Coffee &amp; snacks</li>
    <li><svg width="8" height="8" viewBox="0 0 8 8"><circle cx="4" cy="4" r="4" fill="var(--blue)"/><path d="M2.2 4.1l1.2 1.2 2.4-2.5" stroke="#fff" stroke-width="1" fill="none"/></svg>Everyone welcome</li>
  </ul>
  <footer class="contact-band">
    Location - 180 Birchwood Avenue East Oakridge, ON L0K 2A3<br>
    Phone-555-014-2783 | Email-hello@maplegrovechurch.ca | Website-www.maplegrovechurch.ca
  </footer>
</section>

</body>
</html>
```